Bref créative
Business Cards & Letterhead for a business that owns franchises
HARTWELL HOLDINGS GROUP
Professional
Gregory T. Pennock, Sr.
President & Co-Owner
3852 Fernhollow Bend, SE
Atlanta, GA
Gregory@HartHoldingsGroup.example
www.hartholdingsgroup.example
Our Logo? Be Creative!!
HARTWELL HOLDINGS GROUP LOGO

```html
<!DOCTYPE html>
<html lang="en">
<head>
<meta charset="utf-8">
<title>Hartwell Holdings Group – Business Card</title>
<link rel="stylesheet" href="https://fonts.googleapis.com/css2?family=Cinzel:wght@400;600&family=Open+Sans:wght@400;600&display=swap">
<style>
  :root {
    --bg: #ece8e3;
    --brand-red: #c4161c;
    --brand-red-dark: #9e0f14;
    --brand-red-soft: #d83a3f;
    --swoosh-grey: #8f9398;
    --swoosh-light: #c9ccd0;
    --card-white: #ffffff;
    --card-mist: #e9eaec;
    --text-white: #ffffff;
  }
  * { margin: 0; padding: 0; box-sizing: border-box; }
  html, body { width: 1200px; height: 715px; overflow: hidden; background: var(--bg); }
  .canvas { position: relative; width: 1200px; height: 715px; }

  .card { position: absolute; width: 480px; height: 290px; border-radius: 16px; overflow: hidden;
          box-shadow: 0 10px 28px rgba(0,0,0,.18); }
  .card svg.card-art { position: absolute; inset: 0; }

  .card--front { left: 80px; top: 200px; }
  .card--back  { left: 640px; top: 220px; }

  .brand { position: absolute; left: 34px; top: 30px; display: flex; align-items: center; gap: 16px; }
  .brand-dot { width: 66px; height: 66px; border-radius: 50%; border: 5px solid var(--swoosh-grey); }
  .brand-name { font-family: "Cinzel", serif; font-weight: 400; color: var(--brand-red); line-height: 1; }
  .brand-name .line-main { display: block; font-size: 38px; letter-spacing: 1px; }
  .brand-name .line-sub { display: block; font-size: 15px; letter-spacing: 4px; margin-top: 6px; }

  .holder { position: absolute; left: 22px; top: 190px; color: var(--text-white); }
  .holder-name { font-family: "Cinzel", serif; font-size: 17px; font-weight: 400; }
  .holder-title { font-family: "Open Sans", sans-serif; font-size: 10.5px; margin-top: 2px; }
  .holder-address { font-family: "Open Sans", sans-serif; font-size: 12px; line-height: 1.35; margin-top: 14px; }

  .contacts { position: absolute; left: 262px; top: 172px; list-style: none; color: var(--text-white);
              font-family: "Open Sans", sans-serif; font-size: 10.5px; }
  .contacts li { display: flex; align-items: center; gap: 6px; height: 17px; }
  .contacts li.primary { font-weight: 600; font-size: 12px; }
  .contacts svg { width: 10px; height: 10px; flex: none; }

  .back-mark { position: absolute; left: 40px; top: 70px; display: flex; align-items: center; gap: 0; }
  .back-ring { position: absolute; left: 80px; top: 30px; width: 230px; height: 230px; border-radius: 50%;
               border: 14px solid var(--brand-red-soft); }
  .back-name { position: absolute; left: 40px; top: 108px; font-family: "Cinzel", serif; font-weight: 400;
               color: #f4d6d7; line-height: 1; }
  .back-name .line-main { display: block; font-size: 44px; letter-spacing: 1px; }
  .back-name .line-sub { display: block; font-size: 17px; letter-spacing: 5px; margin-top: 8px; padding-left: 40px; }
</style>
</head>
<body>
<div class="canvas">

  <section class="card card--front" aria-label="Business card front">
    <svg class="card-art" width="480" height="290" viewBox="0 0 480 290">
      <defs>
        <linearGradient id="frontTop" x1="0" y1="0" x2="0" y2="1">
          <stop offset="0" stop-color="var(--card-white)"/>
          <stop offset="1" stop-color="var(--card-mist)"/>
        </linearGradient>
        <linearGradient id="frontRed" x1="0" y1="0" x2="0" y2="1">
          <stop offset="0" stop-color="var(--brand-red)"/>
          <stop offset="1" stop-color="var(--brand-red-dark)"/>
        </linearGradient>
      </defs>
      <rect width="480" height="290" fill="url(#frontTop)"/>
      <path class="swoosh-light" d="M0,138 C150,104 300,170 480,112 L480,130 C300,190 150,124 0,160 Z" fill="var(--swoosh-light)"/>
      <path class="swoosh-grey" d="M0,150 C160,116 300,180 480,125 L480,150 C300,202 160,142 0,176 Z" fill="var(--swoosh-grey)"/>
      <path class="red-field" d="M0,174 C160,140 300,200 480,148 L480,290 L0,290 Z" fill="url(#frontRed)"/>
    </svg>

    <div class="brand">
      <span class="brand-dot"></span>
      <span class="brand-name"><span class="line-main">HARTWELL</span><span class="line-sub">HOLDINGS GROUP</span></span>
    </div>

    <div class="holder">
      <h1 class="holder-name">Gregory T. Pennock, Sr.</h1>
      <p class="holder-title">President &amp; Co-Owner</p>
      <p class="holder-address">3852 Fernhollow Bend, SE<br>Atlanta, GA. 30301</p>
    </div>

    <ul class="contacts">
      <li class="primary"><svg viewBox="0 0 10 10"><path d="M2 0.5h2l1 2.5-1.3 1a6 6 0 0 0 2.3 2.3l1-1.3 2.5 1v2a1 1 0 0 1-1 1A8.5 8.5 0 0 1 1 1.5a1 1 0 0 1 1-1z" fill="#fff"/></svg>888-555-0143</li>
      <li><svg viewBox="0 0 10 10"><path d="M2 0.5h2l1 2.5-1.3 1a6 6 0 0 0 2.3 2.3l1-1.3 2.5 1v2a1 1 0 0 1-1 1A8.5 8.5 0 0 1 1 1.5a1 1 0 0 1 1-1z" fill="#fff"/></svg>404-555-0178</li>
      <li><svg viewBox="0 0 10 10"><rect x="2.5" y="0.5" width="5" height="9" rx="1" fill="#fff"/></svg>678-555-0126</li>
      <li><svg viewBox="0 0 10 10"><rect x="0.5" y="2" width="9" height="6" fill="#fff"/><path d="M0.5 2l4.5 3.5L9.5 2" stroke="var(--brand-red)" fill="none"/></svg>Gregory@HartHoldingsGroup.example</li>
      <li><svg viewBox="0 0 10 10"><circle cx="5" cy="5" r="4.2" fill="none" stroke="#fff"/><path d="M1 5h8M5 0.8v8.4" stroke="#fff" stroke-width=".8"/></svg>www.hartholdingsgroup.example</li>
    </ul>
  </section>

  <section class="card card--back" aria-label="Business card back">
    <svg class="card-art" width="480" height="290" viewBox="0 0 480 290">
      <defs>
        <linearGradient id="backRed" x1="0" y1="0" x2="1" y2="1">
          <stop offset="0" stop-color="var(--brand-red)"/>
          <stop offset="1" stop-color="var(--brand-red-dark)"/>
        </linearGradient>
      </defs>
      <rect width="480" height="290" fill="url(#backRed)"/>
    </svg>
    <span class="back-ring"></span>
    <p class="back-name"><span class="line-main">HARTWELL</span><span class="line-sub">HOLDINGS GROUP</span></p>
  </section>

</div>
</body>
</html>
```